A new presentation to our clients

we are a Real Estate agency, our website is www.lirotama.com and it’s time to have a new, fashion and remarcable Business Card. we want to differentiate ourselves from other companies so we want a business card that differentiates us. we want the business card to impact our customers. in the competitive market that we have today, we have to be different and it is this difference that we seek

Target Market(s)

Real Estate Clients

Contact Information for Business Card

We search a totaly diferent card from the usual

Font styles to use
Sans Serif

Colors
e34197

Requirements
Must have
• Logo, adress, phone contact, e-mail, photo, and our website
Nice to have
• We would like to see a modern business card
Should not have
• Houses or building draws

```html
<!DOCTYPE html>
<html lang="pt">
<head>
<meta charset="utf-8">
<title>Lirotama — Business Card</title>
<link rel="stylesheet" href="https://fonts.googleapis.com/css2?family=Bebas+Neue&family=Work+Sans:wght@400;500;600&display=swap">
<style>
  :root {
    --backdrop: #2b2b2b;
    --card: #1b1b1c;
    --card-edge: #262627;
    --brand-pink: #e3197b;
    --text-light: #f2f2f2;
  }
  * { box-sizing: border-box; margin: 0; padding: 0; }
  html, body { width: 1200px; height: 900px; overflow: hidden; }
  body {
    background: var(--backdrop);
    display: flex;
    flex-direction: column;
    align-items: center;
    justify-content: center;
    gap: 44px;
    font-family: "Work Sans", Arial, sans-serif;
  }
  .card {
    position: relative;
    width: 600px;
    height: 343px;
    background: linear-gradient(135deg, var(--card) 0%, var(--card) 55%, var(--card-edge) 100%);
    border-radius: 3px;
  }
  .card-front {
    display: flex;
    align-items: center;
    justify-content: center;
  }
  .brand-name {
    font-family: "Work Sans", Arial, sans-serif;
    font-weight: 600;
    font-size: 58px;
    letter-spacing: 1px;
    color: var(--brand-pink);
  }
  .contact-block {
    position: absolute;
    top: 120px;
    left: 0;
    right: 0;
    display: flex;
    align-items: stretch;
  }
  .person {
    width: 262px;
    text-align: right;
    padding-right: 18px;
    padding-top: 4px;
  }
  .person-name {
    font-family: "Bebas Neue", Impact, sans-serif;
    font-size: 42px;
    line-height: 1;
    color: var(--brand-pink);
    letter-spacing: 0.5px;
  }
  .person-role {
    font-size: 16px;
    color: var(--text-light);
    margin-top: 2px;
  }
  .divider {
    width: 3px;
    background: var(--brand-pink);
    height: 78px;
  }
  .contact-list {
    list-style: none;
    padding-left: 18px;
    font-size: 17px;
    line-height: 21px;
    color: var(--text-light);
    letter-spacing: 0.5px;
  }
  .contact-list li { display: flex; align-items: center; gap: 10px; }
  .contact-icon { width: 11px; height: 11px; flex: none; }
  .address {
    position: absolute;
    left: 40px;
    bottom: 46px;
    font-size: 17px;
    letter-spacing: 0.6px;
    color: var(--text-light);
  }
</style>
</head>
<body>
  <section class="card card-front">
    <h1 class="brand-name">Lirotama</h1>
  </section>

  <section class="card card-back">
    <div class="contact-block">
      <div class="person">
        <p class="person-name">Daniel Reyes</p>
        <p class="person-role">Director</p>
      </div>
      <div class="divider"></div>
      <ul class="contact-list">
        <li>
          <svg class="contact-icon" viewBox="0 0 12 12"><path fill="#e3197b" d="M2.5 0.5 L4.5 0.5 L5.2 3.2 L3.8 4.3 Q5 7 7.7 8.2 L8.8 6.8 L11.5 7.5 L11.5 9.5 Q11.5 11.5 9.5 11.5 Q0.5 10.5 0.5 2.5 Q0.5 0.5 2.5 0.5Z"/></svg>
          (+351) 210 555 418
        </li>
        <li>
          <svg class="contact-icon" viewBox="0 0 12 12"><rect x="3" y="0.5" width="6" height="3.5" fill="#e3197b"/><rect x="0.5" y="4" width="11" height="5" rx="1" fill="#e3197b"/><rect x="3" y="8" width="6" height="3.5" fill="#e3197b"/></svg>
          (+351) 210 555 419
        </li>
        <li>
          <svg class="contact-icon" viewBox="0 0 12 12"><rect x="0.8" y="2.3" width="10.4" height="7.4" fill="none" stroke="#e3197b" stroke-width="1.2"/><path d="M0.8 2.3 L6 6.5 L11.2 2.3" fill="none" stroke="#e3197b" stroke-width="1.2"/></svg>
          geral@lirotama.com
        </li>
        <li>
          <svg class="contact-icon" viewBox="0 0 12 12"><circle cx="6" cy="6" r="5.2" fill="none" stroke="#e3197b" stroke-width="1.2"/><ellipse cx="6" cy="6" rx="2.3" ry="5.2" fill="none" stroke="#e3197b" stroke-width="1"/><path d="M0.8 6 H11.2" stroke="#e3197b" stroke-width="1"/></svg>
          www.lirotama.com
        </li>
      </ul>
    </div>
    <p class="address">Rua do Miradouro, 57 4410-082, Vila Serena</p>
  </section>
</body>
</html>
```